I am a general contractor in Portland, Or. I would like a clean and simple design layout, maybe using the "didot" font, blue and dark bronze in colors are preferred. On one side of the card, it would be nice to have a logo(attached photo) and business name(KBT Construction). I don't need my job title on the card, just some thing along the lines of "harold pike, general contractor". Thanks much.

Target Market(s)

Adults from 30-55 years old. Middle to upper class.

Industry/Entity Type

Contractor

Contact Information for Business Card

KBT Construction
Harold M. Pike
2943 NE 71st Ave.
Portland, Or. 97288
503.627.9184

Font styles to use
Other font styles liked:
• didot

Colors
3277b5
7f7f7f

Requirements
Should not have
• Too much going on.

```html
<!DOCTYPE html>
<html lang="en">
<head>
<meta charset="utf-8">
<title>KBT Construction – Business Card</title>
<link rel="stylesheet" href="https://fonts.googleapis.com/css2?family=GFS+Didot&family=Montserrat:wght@300;400&display=swap">
<style>
  :root {
    --page-bg: #e9e6e1;
    --card-black: #0d0e10;
    --card-black-edge: #1c1e22;
    --brand-blue: #3277b5;
    --brand-blue-deep: #114178;
    --brand-blue-light: #3f86c4;
    --brand-grey: #7f7f7f;
    --text-light: #e9edf2;
    --text-soft: #c9d2dc;
  }
  * { box-sizing: border-box; margin: 0; padding: 0; }
  html, body {
    width: 1200px;
    height: 1023px;
    overflow: hidden;
    background: var(--page-bg);
  }
  .canvas {
    position: relative;
    width: 1200px;
    height: 1023px;
  }
  .card {
    position: absolute;
    width: 600px;
    height: 343px;
    border-radius: 4px;
    overflow: hidden;
    box-shadow: 0 10px 28px rgba(0,0,0,0.22);
  }

  /* Contact side */
  .card-contact {
    left: 70px;
    top: 90px;
    background: linear-gradient(150deg, var(--card-black-edge) 0%, var(--card-black) 55%);
  }
  .brand-mark {
    position: absolute;
    left: 40px;
    top: 150px;
    display: flex;
    align-items: center;
    gap: 16px;
  }
  .brand-dot {
    width: 74px;
    height: 74px;
    border-radius: 50%;
    background: var(--brand-blue);
  }
  .brand-mark-name {
    font-family: "GFS Didot", "Didot", serif;
    font-size: 26px;
    letter-spacing: 1.5px;
    color: var(--brand-blue);
    text-transform: uppercase;
  }
  .contact-block {
    position: absolute;
    right: 40px;
    top: 38px;
    text-align: right;
  }
  .contact-name {
    font-family: "GFS Didot", "Didot", serif;
    font-size: 30px;
    color: var(--brand-blue);
    margin-bottom: 10px;
  }
  .contact-line {
    font-family: "Montserrat", sans-serif;
    font-weight: 300;
    font-size: 15px;
    letter-spacing: 0.5px;
    color: var(--text-light);
    line-height: 1.55;
  }
  .contact-address {
    position: absolute;
    right: 40px;
    bottom: 30px;
    font-family: "Montserrat", sans-serif;
    font-weight: 300;
    font-size: 14px;
    letter-spacing: 1px;
    color: var(--text-soft);
    text-transform: uppercase;
  }

  /* Brand side */
  .card-brand {
    left: 530px;
    top: 580px;
    background: radial-gradient(ellipse at 60% 40%, var(--brand-blue-light) 0%, var(--brand-blue) 40%, var(--brand-blue-deep) 100%);
  }
  .brand-symbol-spot {
    position: absolute;
    left: 74px;
    top: 120px;
    width: 100px;
    height: 100px;
    border-radius: 50%;
    background: #f4f6f8;
  }
  .brand-name {
    position: absolute;
    left: 215px;
    top: 134px;
    font-family: "GFS Didot", "Didot", serif;
    font-size: 34px;
    letter-spacing: 1.5px;
    color: #ffffff;
    text-transform: uppercase;
  }
  .brand-tagline {
    position: absolute;
    left: 217px;
    top: 184px;
    display: flex;
    align-items: center;
    gap: 10px;
    font-family: "Montserrat", sans-serif;
    font-weight: 300;
    font-size: 15px;
    letter-spacing: 0.5px;
    color: var(--text-light);
  }
  .tagline-sep {
    width: 6px;
    height: 6px;
    border-radius: 50%;
    background: #0b1a2c;
  }
</style>
</head>
<body>
<main class="canvas">

  <section class="card card-contact" aria-label="Business card, contact side">
    <div class="brand-mark">
      <span class="brand-dot"></span>
      <span class="brand-mark-name">KBT Construction</span>
    </div>
    <div class="contact-block">
      <p class="contact-name">Harold M. Pike</p>
      <p class="contact-line">503.627.9184</p>
      <p class="contact-line">harold@kbtbuild.net</p>
    </div>
    <p class="contact-address">2943 NE 71st Ave. Portland, Or. 97288</p>
  </section>

  <section class="card card-brand" aria-label="Business card, brand side">
    <span class="brand-symbol-spot"></span>
    <h1 class="brand-name">KBT Construction</h1>
    <p class="brand-tagline">
      <span>Harold Pike</span>
      <span class="tagline-sep"></span>
      <span>General Contractor</span>
    </p>
  </section>

</main>
</body>
</html>
```